Private lender of mortgages and rent to own housing

need a website that reflects real estate especially mortgage lending and rent to own houses..
Sections as follows
Home About Types of mortgages Rent to own Contact us
Target Market(s)
consumers who require non traditonal mortgages
Industry/Entity Type
Mortgage
Coding
Coded - Design and coding required
Number of Pages Required
4 page
Font styles to use
Sans Serif
Colors
Designer to choose colors to be used in the design.
Requirements
Must have
- background pictures on pages. with nice picture on homepage of houses or a community
Nice to have
- contact us form i supplied a ink to

```html
<!DOCTYPE html>
<html lang="en">
<head>
<meta charset="utf-8">
<title>Northgate Home Lending</title>
<link rel="stylesheet" href="https://fonts.googleapis.com/css2?family=Montserrat:wght@400;500;600;700&family=Open+Sans:wght@400;600;700&display=swap">
<style>
:root{
  --navy:#2a2665;
  --blue:#0a5196;
  --sky:#1b87c9;
  --accent:#1a8ad0;
  --ink:#333;
  --muted:#6d6d6d;
  --light:#f0f0f0;
  --footer:#5f5f5f;
  --white:#fff;
}
*{box-sizing:border-box;margin:0;padding:0}
html,body{width:1200px;height:2436px;overflow:hidden}
body{position:relative;background:var(--white);font-family:"Open Sans",Arial,sans-serif;color:var(--ink)}
.abs{position:absolute}
h1,h2,h3,h4,.nav,.btn{font-family:"Montserrat",Arial,sans-serif}

/* header */
.header{left:0;top:0;width:1200px;height:72px;background:var(--navy)}
.brand-plate{left:0;top:0;width:440px;height:72px;background:var(--white);clip-path:polygon(0 0,100% 0,370px 100%,0 100%)}
.brand{left:156px;top:44px;display:flex;align-items:center;gap:8px;font-family:"Montserrat",sans-serif;font-weight:700;font-size:12.5px;color:var(--navy);letter-spacing:.2px}
.brand .mark{width:12px;height:12px;background:var(--navy)}
.call{right:156px;top:16px;color:var(--white);font-family:"Montserrat",sans-serif;font-weight:700;font-size:14px}
.nav{left:433px;top:44px;display:flex;color:var(--white);font-size:12px;font-weight:500}
.nav span{padding:0 17px;border-left:1px solid rgba(255,255,255,.8);line-height:12px}
.nav span:first-child{border-left:0;padding-left:0;position:relative}
.nav .active::after{content:"";position:absolute;left:0;right:17px;bottom:-8px;height:2px;background:var(--white)}

/* hero */
.hero{left:0;top:72px;width:1200px;height:432px;background:linear-gradient(180deg,#8a8f98 0%,#a79a86 40%,#6f5b45 70%,#3f5a2e 100%)}
.hero-shade{left:0;top:72px;width:1200px;height:432px;background:linear-gradient(90deg,rgba(0,0,0,.35),rgba(0,0,0,0) 60%)}
.hero-block h1{left:154px;top:226px;color:var(--white);font-size:25px;font-weight:700;line-height:30px;text-shadow:0 1px 3px rgba(0,0,0,.4)}
.btn-primary{background:var(--accent);color:var(--white);font-size:11px;font-weight:600;display:flex;align-items:center;justify-content:center}
.hero-block .cta{left:154px;top:312px;width:152px;height:31px}
.arrow{top:276px;width:20px;height:30px}

/* about */
.about h2{left:154px;top:576px;font-size:25px;font-weight:400;color:var(--ink)}
.about h2 b,.section-title b{color:var(--accent);font-weight:600}
.about .rule{left:133px;top:604px;width:150px;height:1px;background:#999}
.about p{left:154px;width:530px;font-size:12px;line-height:18px;color:var(--muted)}
.about .lead{left:154px;top:766px;font-size:13px;font-weight:600;color:var(--ink)}
.btn-outline{border:1.5px solid var(--accent);color:var(--ink);font-size:11px;font-weight:600;display:flex;align-items:center;justify-content:center}
.about .more{left:154px;top:812px;width:130px;height:33px}
.about-photo{left:740px;top:504px;width:304px;height:389px;background:linear-gradient(180deg,#a9c8e6 0%,#b07a4c 45%,#7f5a3a 65%,#4f8a33 100%)}

/* types */
.types{left:0;top:893px;width:1200px;height:273px;background:var(--blue)}
.types-block .section-title{left:0;width:1200px;top:938px;text-align:center;color:var(--white);font-size:24px;font-weight:400}
.types-block .section-title b{color:var(--white)}
.types-block .rule{left:154px;top:1007px;width:890px;height:1px;background:rgba(255,255,255,.35)}
.tile{top:1008px;width:297px;height:158px;display:flex;flex-direction:column;align-items:center;color:var(--white)}
.tile svg{margin-top:32px}
.tile h3{font-size:15px;font-weight:600;margin-top:10px}
.tile.current{background:var(--sky)}
.notch{left:584px;top:1165px;width:0;height:0;border-left:16px solid transparent;border-right:16px solid transparent;border-top:16px solid var(--sky)}

/* bridge */
.bridge{left:0;top:1166px;width:1200px;height:422px;background:var(--light)}
.section-title{font-size:24px;font-weight:400}
.bridge-block h2{left:0;width:1200px;top:1208px;text-align:center;color:var(--accent);font-size:24px;font-weight:600}
.bridge-block .intro{left:170px;width:860px;top:1256px;text-align:center;font-size:12.5px;line-height:19.5px;color:var(--muted)}
.bridge-block .divider{left:308px;top:1341px;width:584px;height:1px;background:#ccc}
.col h4{font-size:14px;font-weight:600;color:var(--ink);display:flex;align-items:center;gap:12px}
.col h4::before{content:"";width:26px;height:2px;background:var(--ink)}
.col p{margin-top:14px;font-size:12.5px;line-height:19px;color:var(--muted)}
.col.problem{left:156px;top:1370px;width:415px}
.col.solution{left:636px;top:1370px;width:415px}
.bridge-block .vline{left:601px;top:1374px;width:1px;height:164px;background:#ccc}

/* rent to own */
.rto .section-title{left:0;width:1200px;top:1624px;text-align:center;color:var(--ink)}
.rto .title-rule{left:567px;top:1660px;width:160px;height:2px;background:var(--accent)}
.rto h3{left:0;width:1200px;top:1694px;text-align:center;font-size:15px;font-weight:600;color:var(--ink)}
.rto .intro{left:218px;width:764px;top:1725px;text-align:center;font-size:12.5px;line-height:19.5px;color:var(--muted)}
.step{top:1827px;width:228px;display:flex;flex-direction:column;align-items:center;text-align:center}
.step .ico{width:88px;height:88px;border-radius:50%;border:1.5px solid var(--accent);display:flex;align-items:center;justify-content:center}
.step .ico.filled{background:var(--accent)}
.step h4{margin-top:20px;font-family:"Montserrat",sans-serif;font-size:15px;font-weight:500;color:var(--ink)}
.step p{margin-top:12px;width:190px;font-size:12px;line-height:17.5px;color:var(--muted)}
.step .read{margin-top:11px;font-size:11px;font-weight:600;color:var(--ink)}
.step .read.on{color:var(--accent);text-decoration:underline}
.rto .apply{left:421px;top:2080px;width:360px;height:32px}

/* footer */
footer{color:var(--white)}
.footer{left:0;top:2160px;width:1200px;height:276px;background:var(--footer)}
.fcol{top:2204px;width:260px;display:flex;flex-direction:column;align-items:center;text-align:center;color:var(--white)}
.fcol svg{height:38px}
.fcol .big{margin-top:12px;font-family:"Montserrat",sans-serif;font-size:15px;font-weight:600}
.fcol .small{margin-top:12px;font-size:11.5px;line-height:16px}
.fcol a{color:var(--white);font-size:11.5px;text-decoration:underline}
footer .fline{left:154px;top:2327px;width:890px;height:1px;background:rgba(255,255,255,.3)}
.fnav{left:0;width:1200px;top:2342px;display:flex;justify-content:center;font-family:"Montserrat",sans-serif;font-size:11.5px;color:var(--white)}
.fnav span{padding:0 18px;border-left:1px solid rgba(255,255,255,.8);line-height:12px}
.fnav span:first-child{border-left:0;color:var(--accent)}
.copy{left:154px;top:2395px;font-size:11px;color:var(--white)}
.copy u{color:var(--white)}
.social{top:2384px;width:36px;height:36px;border-radius:50%;border:1.5px solid rgba(255,255,255,.5)}
.social.on{background:var(--accent);border-color:var(--accent)}
.totop{left:1010px;top:2388px;width:32px;height:32px;border:1.5px solid var(--accent);display:flex;align-items:center;justify-content:center}
</style>
</head>
<body>

<header>
  <div class="abs header"></div>
  <div class="abs brand-plate"></div>
  <div class="abs brand"><span class="mark"></span>Northgate Home Lending</div>
  <div class="abs call">Call Us: 555 - 014 - 2286</div>
  <nav class="abs nav">
    <span class="active">Home</span><span>About us</span><span>Types of mortgages</span><span>Rent to Own</span><span>FAQ</span><span>Contact us</span>
  </nav>
</header>

<section class="hero-block">
  <div class="abs hero" role="img" aria-label="Modern luxury house at dusk with lit windows, reflecting pool, lawn and mountains behind"></div>
  <div class="abs hero-shade"></div>
  <h1 class="abs">Private Lender of Mortgages and<br>Rent to Own Housing</h1>
  <div class="abs btn btn-primary cta">Rent to Own a Home</div>
  <svg class="abs arrow" style="left:58px" viewBox="0 0 20 30"><path d="M15 3 L4 15 L15 27" fill="none" stroke="#fff" stroke-width="2"/></svg>
  <svg class="abs arrow" style="left:1124px" viewBox="0 0 20 30"><path d="M5 3 L16 15 L5 27" fill="none" stroke="#fff" stroke-width="2"/></svg>
</section>

<section class="about">
  <h2 class="abs">About <b>Us</b></h2>
  <div class="abs rule"></div>
  <p class="abs" style="top:630px">Northgate Home Lending is a private lender of 1st,2nd, construction and bridge mortgages in Simcoe County area. NHL offers a wide array of financing options to provide assistance to those of you that do not meet the bank's criteria.</p>
  <p class="abs" style="top:696px">The reasons could range from bruised credit to inability to provide the banks with the required documentation to meet income qualification guidelines or simply you need a short term solution and the bank isn't an option.</p>
  <div class="abs lead">We are here to help in any way that we can.</div>
  <div class="abs btn btn-outline more">Discover More</div>
  <div class="abs about-photo" role="img" aria-label="Wooden modern home with stone garden path and green lawn"></div>
</section>

<section class="types-block">
  <div class="abs types"></div>
  <h2 class="abs section-title">Types of <b>Mortgages</b></h2>
  <div class="abs rule"></div>
  <div class="abs tile" style="left:154px">
    <svg width="80" height="76" viewBox="0 0 80 76">
      <path d="M36 8 A30 30 0 1 0 66 40 L36 40 Z" fill="#fff"/>
      <path d="M41 3 A30 30 0 0 1 71 33 L41 33 Z" fill="#fff"/>
      <path d="M36 40 L14 62 M36 40 L36 70" stroke="#0a5196" stroke-width="3"/>
      <circle cx="56" cy="18" r="10" fill="#0a5196"/>
      <text x="56" y="23" text-anchor="middle" fill="#fff" font-family="Montserrat,sans-serif" font-weight="700" font-size="14">$</text>
    </svg>
    <h3>Debt Consolidation</h3>
  </div>
  <div class="abs tile current" style="left:451px">
    <svg width="80" height="76" viewBox="0 0 80 76">
      <path d="M40 6 L4 38 L12 38 L12 70 L68 70 L68 38 L76 38 Z" fill="#fff"/>
      <rect x="33" y="44" width="14" height="26" fill="#1b87c9"/>
    </svg>
    <h3>Bridge Financing</h3>
  </div>
  <div class="notch abs"></div>
  <div class="abs tile" style="left:747px">
    <svg width="80" height="76" viewBox="0 0 80 76">
      <path d="M24 10 L4 30 L10 30 L10 70 L38 70 L38 30 L44 30 Z" fill="none" stroke="#fff" stroke-width="3"/>
      <rect x="15" y="52" width="6" height="18" fill="#fff"/><rect x="25" y="44" width="6" height="26" fill="#fff"/>
      <rect x="44" y="46" width="7" height="24" fill="#fff"/><rect x="55" y="38" width="7" height="32" fill="#fff"/><rect x="66" y="28" width="7" height="42" fill="#fff"/>
      <path d="M14 42 L34 28 L48 36 L72 12" fill="none" stroke="#fff" stroke-width="3.5"/>
      <path d="M62 10 L76 8 L74 22 Z" fill="#fff"/>
    </svg>
    <h3>Equity take out</h3>
  </div>
</section>

<section class="bridge-block">
  <div class="abs bridge"></div>
  <h2 class="abs">Bridge Financing</h2>
  <p class="abs intro">Are you or your client looking forward to moving into that new property you just purchased, but your possession date is earlier than the sale of your current property? Often, possession dates don't align in a way that is most convenient, and our bridge financing option will provide the peace of mind while in transition.</p>
  <div class="abs divider"></div>
  <div class="abs col problem">
    <h4>Problem</h4>
    <p>Are you or your client looking forward to moving into that new property you just purchased, but your Loans are often too short term You don't want to lose the sales of your property while waiting for financing Existing lenders are not willing or able to bridge the purchase with your existing equity Limited and restrictive conditions cause penalties at traditional financial institutions Your house is listed but hasn't sold yet.</p>
  </div>
  <div class="abs vline"></div>
  <div class="abs col solution">
    <h4>Solution</h4>
    <p>We can help you close the sale of your purchase before the property you are moving out of sells, or before its possession date if it is sold. We offer a short term loan to bridge the gap for you, allowing a less stressful transition between homes. We can also help you take advantage of your prepayment privileges on the house you are selling to help reduce your prepayment penalty.</p>
  </div>
</section>

<section class="rto">
  <h2 class="abs section-title">Rent to <b>Own a Home</b></h2>
  <div class="abs title-rule"></div>
  <h3 class="abs">We Can Put You in Your Own Home Today</h3>
  <p class="abs intro">We know life sometimes delivers challenges and it can be hard to get back on track once you have dealt with challenges. Maybe you have been through a divorce, bankruptcy, consumer proposal, loss of job, work place injury, new to the country, self-employed or some credit related challenges...</p>

  <div class="abs step" style="left:144px">
    <div class="ico"><svg width="44" height="48" viewBox="0 0 44 48"><rect x="11" y="3" width="20" height="34" rx="3" fill="none" stroke="#333" stroke-width="2.2"/><circle cx="21" cy="18" r="6" fill="none" stroke="#333" stroke-width="2"/><path d="M9 28 Q4 34 10 44 L28 46 L34 34 L24 30" fill="none" stroke="#333" stroke-width="2.2"/></svg></div>
    <h4>Down Payment</h4>
    <p>We know life sometimes delivers challenges and it can be hard to get...</p>
    <div class="read">Read More</div>
  </div>
  <div class="abs step" style="left:372px">
    <div class="ico"><svg width="46" height="46" viewBox="0 0 46 46"><path d="M3 22 L20 8 L30 16 M7 19 L7 42 L30 42 L30 30" fill="none" stroke="#333" stroke-width="2.4"/><rect x="14" y="30" width="8" height="12" fill="#333"/><circle cx="33" cy="16" r="10" fill="#333"/><text x="33" y="21" text-anchor="middle" fill="#fff" font-family="Montserrat,sans-serif" font-weight="700" font-size="13">$</text></svg></div>
    <h4>Household Income</h4>
    <p>Steady, provable household income that can support the price of...</p>
    <div class="read on">Read More</div>
  </div>
  <div class="abs step" style="left:601px">
    <div class="ico filled"><svg width="46" height="46" viewBox="0 0 46 46"><rect x="8" y="16" width="26" height="16" rx="2" fill="#fff"/><rect x="8" y="20" width="26" height="3" fill="#1a8ad0"/><path d="M18 10 Q30 4 36 12 M33 6 L37 12 L31 13" fill="none" stroke="#fff" stroke-width="2.4"/><path d="M28 38 Q16 44 10 36 M13 42 L9 36 L15 35" fill="none" stroke="#fff" stroke-width="2.4"/></svg></div>
    <h4>Credit Report</h4>
    <p>Although your credit won't necessarily disqualify you from our rent to...</p>
    <div class="read">Read More</div>
  </div>
  <div class="abs step" style="left:828px">
    <div class="ico"><svg width="48" height="48" viewBox="0 0 48 48"><path d="M24 3 L45 24 L24 45 L3 24 Z" fill="none" stroke="#333" stroke-width="2.4"/><path d="M24 13 L13 23 L16 23 L16 33 L32 33 L32 23 L35 23 Z" fill="none" stroke="#333" stroke-width="2.2"/><rect x="20" y="24" width="3.5" height="3.5" fill="#333"/><rect x="24.5" y="24" width="3.5" height="3.5" fill="#333"/><rect x="20" y="28.5" width="3.5" height="3.5" fill="#333"/><rect x="24.5" y="28.5" width="3.5" height="3.5" fill="#333"/></svg></div>
    <h4>Selecting a House</h4>
    <p>May not seem like a strong determining factor overall for qualifying for rent to ...</p>
    <div class="read">Read More</div>
  </div>

  <div class="abs btn btn-primary apply">Submit Application for Rent-To-Own A Home Program</div>
</section>

<footer>
  <div class="abs footer"></div>
  <div class="abs fcol" style="left:224px">
    <svg width="38" height="38" viewBox="0 0 38 38"><path d="M8 5 L14 5 L17 13 L13 16 Q16 23 22 26 L25 22 L33 25 L33 31 Q33 34 29 34 Q6 32 4 9 Q4 5 8 5 Z" fill="none" stroke="#fff" stroke-width="2"/><path d="M22 4 Q33 5 34 16 M22 10 Q28 10 28 16" fill="none" stroke="#fff" stroke-width="2"/></svg>
    <div class="big">555-014-2286</div>
    <a>Email Us</a>
  </div>
  <div class="abs fcol" style="left:470px">
    <svg width="30" height="38" viewBox="0 0 30 38"><path d="M15 36 Q3 22 3 14 A12 12 0 0 1 27 14 Q27 22 15 36 Z" fill="none" stroke="#fff" stroke-width="2"/><circle cx="15" cy="14" r="4.5" fill="none" stroke="#fff" stroke-width="2"/></svg>
    <div class="small">4417 Cedar Ridge Rd.<br>Lakeview, ON 55120</div>
  </div>
  <div class="abs fcol" style="left:718px">
    <svg width="30" height="38" viewBox="0 0 30 38"><path d="M7 11 Q7 3 15 3 Q23 3 23 11 Q23 16 17 19 Q15 21 15 26" fill="none" stroke="#fff" stroke-width="2.2"/><circle cx="15" cy="33" r="2" fill="#fff"/></svg>
    <div class="big">Need Help?</div>
    <a>Contact Us</a>
  </div>
  <div class="abs fline"></div>
  <nav class="abs fnav"><span>Home</span><span>About us</span><span>Types of mortgages</span><span>Rent to Own</span><span>FAQ</span><span>Contact us</span></nav>
  <div class="abs copy">© 2017 True <u>Northgate Home Lending</u>. All right reserved</div>
  <div class="abs social" style="left:810px"></div>
  <div class="abs social" style="left:851px"></div>
  <div class="abs social on" style="left:891px"></div>
  <div class="abs social" style="left:934px"></div>
  <div class="abs totop"><svg width="14" height="14" viewBox="0 0 14 14"><path d="M7 13 L7 2 M2 7 L7 2 L12 7" fill="none" stroke="#1a8ad0" stroke-width="2"/></svg></div>
</footer>

</body>
</html>
```